Yacht Charter Broker needs a magazine page design

We are a travel agent for yachts called Velmoria Yacht Charters. www.velmoriacharters.example We are advertising in a magazine at the grand pacer equine fair - https://plgequinefair.example/ - and need a high-end luxury feeling magazine page.

Target Market(s)

Vacation goers looking to charter a crewed yacht.

Industry/Entity Type

Travel Agent

Requirements
Must have
• luxury feel. logo. website and social media icons if you feel necessary. Our motto is: Inhale. Exhale. Sail.
• Catamaran picture, snorkeling and other island, water looking pictures.
Nice to have
• Open to your design.
Should not have
• Nothing comes to mind.

```html
<!DOCTYPE html>
<html lang="en">
<head>
<meta charset="utf-8">
<title>Velmoria Yacht Charters – Magazine Page</title>
<link rel="stylesheet" href="https://fonts.googleapis.com/css2?family=Cinzel:wght@400&family=Raleway:wght@300;400;500;800&display=swap">
<style>
  :root {
    --canvas: #d9d9d7;
    --ink: #121316;
    --sea-deep: #0b2d57;
    --sea-mid: #134a85;
    --sea-light: #1f5f9e;
    --white: #ffffff;
    --soft-white: #eef2f7;
  }
  * { margin: 0; padding: 0; box-sizing: border-box; }
  html, body { width: 1200px; height: 1200px; overflow: hidden; background: var(--canvas); }
  .page {
    position: absolute; left: 207px; top: 0;
    width: 786px; height: 1200px;
    background: var(--ink); overflow: hidden;
    font-family: "Raleway", sans-serif; color: var(--white);
  }
  .masthead { position: absolute; left: 0; top: 0; width: 100%; height: 193px; }
  .brand-name {
    position: absolute; left: 0; right: 0; top: 62px; text-align: center;
    font-family: "Cinzel", serif; font-weight: 400; font-size: 54px; letter-spacing: 8px;
  }
  .brand-tagline {
    position: absolute; right: 192px; top: 128px;
    font-family: "Cinzel", serif; font-size: 14px; letter-spacing: 3px;
  }
  .hero {
    position: absolute; left: 0; top: 193px; width: 100%; height: 731px;
    background:
      radial-gradient(ellipse at 30% 50%, var(--sea-light) 0%, transparent 60%),
      linear-gradient(160deg, var(--sea-mid) 0%, var(--sea-deep) 100%);
  }
  .motto { position: absolute; right: 46px; font-weight: 300; line-height: 1; }
  .motto--inhale { top: 236px; font-size: 108px; }
  .motto--exhale { top: 372px; font-size: 108px; right: 42px; }
  .motto--sail { top: 480px; font-size: 172px; font-weight: 800; right: 40px; letter-spacing: -2px; }
  .decor-lines { position: absolute; left: 0; top: 0; width: 786px; height: 1200px; pointer-events: none; }
  .claim {
    position: absolute; left: 480px; width: 300px; top: 668px;
    text-align: center; font-weight: 500; font-size: 22px; line-height: 30px; text-transform: uppercase;
  }
  .intro-line { position: absolute; font-size: 15.5px; line-height: 1; color: var(--soft-white); white-space: nowrap; }
  .footer-copy {
    position: absolute; left: 26px; right: 28px; top: 980px;
    font-size: 16px; line-height: 25.5px; text-align: center; color: var(--soft-white);
  }
  .social { position: absolute; top: 1122px; left: 562px; display: flex; gap: 18px; }
  .social-dot { width: 36px; height: 36px; border: 2px solid var(--white); border-radius: 50%; }
</style>
</head>
<body>
  <article class="page">
    <header class="masthead">
      <div class="brand-name">VELMORIA</div>
      <div class="brand-tagline">YACHT CHARTER BROKER</div>
    </header>

    <section class="hero" role="img" aria-label="Aerial photograph of a white sailing catamaran cruising across deep blue open sea"></section>

    <div class="motto motto--inhale">INHALE</div>
    <div class="motto motto--exhale">EXHALE</div>
    <div class="motto motto--sail">SAIL</div>

    <svg class="decor-lines" viewBox="0 0 786 1200" aria-hidden="true">
      <line x1="550" y1="270" x2="508" y2="400" stroke="#ffffff" stroke-width="3"/>
      <line x1="462" y1="672" x2="274" y2="934" stroke="#ffffff" stroke-width="3"/>
    </svg>

    <h2 class="claim">Velmoria is the world's foremost in yacht chartering</h2>

    <p class="intro">
      <span class="intro-line" style="left:412px;top:790px">Celebrities and the super rich have long used</span>
      <span class="intro-line" style="left:394px;top:816px">yachts as a way of combining luxury and privacy,</span>
      <span class="intro-line" style="left:375px;top:842px">and a growing market has seen it become not only</span>
      <span class="intro-line" style="left:357px;top:867px">popular, but accessible, for those looking to</span>
      <span class="intro-line" style="left:339px;top:893px">experience groundbreaking travel.</span>
    </p>

    <p class="footer-copy">Forget about the tight schedule of a cruise ship and dealing with multiple reservations of hotels and restaurants - Velmoria Yacht Charters offers an adventure like no other, with freedom AND flexibility. Custom-tailored to the exact vacation you and your guests want to experience, we also put together a professional crew dedicated to perfecting your experience. Luxury accomodations, relaxation like you've never felt, breathtaking views, gourmet cuisine and endless activities. Inhale, Exhale, Sail - with Velmoria Yacht Charters.</p>

    <div class="social" aria-label="Social media">
      <span class="social-dot"></span>
      <span class="social-dot"></span>
      <span class="social-dot"></span>
      <span class="social-dot"></span>
    </div>
  </article>
</body>
</html>
```